Email Signature Block Design for Law Firm

I would like you to create a similar signature block for my law firm . I saw the email signature block attached as image002.png and wanted a similar design for my law firm. I want to be able to swap the portraits for each of my staff from the final design. Our law firm colors are black, gold, white, red.

Industry/Entity Type

Law

Requirements
Nice to have
• i like the red circle in around the photo in the 8 copper bench design. The 9 Copper Bench desgn is what inspired me to have a signature block design for my firm.

```html
<!DOCTYPE html>
<html lang="en">
<head>
<meta charset="utf-8">
<title>The Hale Firm – Email Signatures</title>
<link href="https://fonts.googleapis.com/css2?family=Cinzel:wght@600;700&family=Montserrat:wght@600;700&family=Libre+Baskerville:wght@700&display=swap" rel="stylesheet">
<style>
:root{
  --page:#ffffff;
  --ink:#000000;
  --navy-deep:#05051a;
  --navy:#0d1a5c;
  --navy-ring:#13276b;
  --gold:#e3940b;
  --gold-brand:#d39a2c;
  --gold-light:#d8b571;
  --gold-dark:#8a6420;
  --white:#ffffff;
  --portrait:#e9e4de;
}
*{box-sizing:border-box;margin:0;padding:0}
html,body{width:1200px;height:1200px;overflow:hidden;background:var(--page)}
.canvas{position:relative;width:1200px;height:1200px}
.signature{position:absolute;left:191px;width:825px;height:275px;overflow:hidden;background:var(--ink)}
.signature--navy{top:272px}
.signature--gold{top:661px}
.backdrop{position:absolute;left:0;width:100%}
.signature--navy .backdrop{top:0;height:203px;background:radial-gradient(ellipse at 30% 40%,#1b2470 0%,var(--navy) 35%,var(--navy-deep) 100%)}
.signature--gold .backdrop{top:72px;height:131px;background:linear-gradient(90deg,var(--gold-dark) 0%,var(--gold-light) 30%,#cfae6c 55%,var(--gold-light) 75%,#c29a52 100%)}
.brand-mark{position:absolute;left:10px;top:14px;width:68px;font-family:'Cinzel',serif;font-weight:700;font-size:9px;line-height:1.1;color:var(--gold-brand);text-align:center}
.brand-mark .square{display:block;width:24px;height:24px;margin:0 auto 5px;background:var(--gold-brand)}
.signature--gold .brand-mark{left:12px;top:6px}
.name{position:absolute;left:63px;top:98px;font-family:'Cinzel',serif;font-weight:700;font-size:24px;line-height:1;color:var(--white)}
.name .suffix{display:block;font-size:19px;margin-top:4px}
.signature--gold .name{left:40px;top:112px;color:var(--ink)}
.contacts{position:absolute;left:586px;top:100px;font-family:'Montserrat',sans-serif;font-weight:700;font-size:15.5px;color:var(--white);list-style:none}
.contacts li{display:flex;align-items:center;gap:8px;height:22px}
.contacts svg{width:16px;height:16px;flex:none}
.signature--gold .contacts{left:561px;top:111px;color:var(--ink);font-size:16.5px}
.signature--gold .contacts li{height:24px}
.firm-block{position:absolute;left:57px;top:210px;width:183px;text-align:center;color:var(--white)}
.firm-name{font-family:'Cinzel',serif;font-weight:600;font-size:15px;line-height:1}
.firm-name small{font-size:10px}
.firm-tag{display:flex;align-items:center;gap:4px;font-family:'Montserrat',sans-serif;font-size:6px;letter-spacing:3.2px;margin:3px 0 1px}
.firm-tag::before,.firm-tag::after{content:"";flex:1;height:1px;background:var(--white)}
.firm-web,.firm-phone{font-family:'Libre Baskerville',serif;font-weight:700;font-size:13px;line-height:14px}
.firm-web{letter-spacing:-.4px}
.call-button{position:absolute;left:608px;top:226px;width:119px;height:30px;border-radius:5px;background:var(--gold);font-family:'Montserrat',sans-serif;font-weight:700;font-size:20px;line-height:30px;text-align:center;color:var(--ink)}
.portrait-ring{position:absolute;left:292px;top:17px;width:231px;height:231px;border-radius:50%;display:flex;align-items:center;justify-content:center}
.signature--navy .portrait-ring{background:var(--navy-ring)}
.signature--gold .portrait-ring{background:var(--gold)}
.portrait{width:196px;height:196px;border-radius:50%;background:radial-gradient(circle at 50% 40%,#ffffff 0%,var(--portrait) 55%,#2a2622 56%,#151312 100%)}
</style>
</head>
<body>
<main class="canvas">

  <section class="signature signature--navy">
    <div class="backdrop" role="img" aria-label="Dark navy background of scattered banknotes"></div>
    <div class="brand-mark"><span class="square"></span>The Hale Firm</div>
    <h2 class="name">Marcus Hale<span class="suffix">Esq.</span></h2>
    <ul class="contacts">
      <li><svg viewBox="0 0 16 16"><circle cx="8" cy="8" r="8" fill="currentColor"/><path d="M5 4.2l1.5-.4 1 2.2-1 .8c.5 1.2 1.3 2 2.5 2.6l.8-1 2.2 1-.4 1.5c-3.4.3-6.9-3.2-6.6-6.7z" fill="#05051a"/></svg>555-014-2290</li>
      <li><svg viewBox="0 0 16 16" fill="none" stroke="currentColor" stroke-width="1.2"><circle cx="8" cy="8" r="7"/><circle cx="8" cy="8" r="4"/><ellipse cx="8" cy="8" rx="1.8" ry="4"/><path d="M4 8h8"/></svg>standwithjustice.com</li>
    </ul>
    <div class="firm-block">
      <p class="firm-name">The Hale Firm, <small>PLLC</small></p>
      <p class="firm-tag">Attorneys At Law</p>
      <p class="firm-web">STANDWITHJUSTICE.COM</p>
      <p class="firm-phone">(555) 014-2290</p>
    </div>
    <div class="call-button">call now</div>
    <div class="portrait-ring"><div class="portrait" role="img" aria-label="Staff portrait photo"></div></div>
  </section>

  <section class="signature signature--gold">
    <div class="backdrop" role="img" aria-label="Gold-toned photo of a columned courthouse"></div>
    <div class="brand-mark"><span class="square"></span>The Hale Firm</div>
    <h2 class="name">Marcus Hale<span class="suffix">Esq.</span></h2>
    <ul class="contacts">
      <li><svg viewBox="0 0 16 16"><circle cx="8" cy="8" r="8" fill="currentColor"/><path d="M5 4.2l1.5-.4 1 2.2-1 .8c.5 1.2 1.3 2 2.5 2.6l.8-1 2.2 1-.4 1.5c-3.4.3-6.9-3.2-6.6-6.7z" fill="#d8b571"/></svg>555-014-2290</li>
      <li><svg viewBox="0 0 16 16" fill="none" stroke="currentColor" stroke-width="1.2"><circle cx="8" cy="8" r="7"/><circle cx="8" cy="8" r="4"/><ellipse cx="8" cy="8" rx="1.8" ry="4"/><path d="M4 8h8"/></svg>standwithjustice.com</li>
    </ul>
    <div class="firm-block">
      <p class="firm-name">The Hale Firm, <small>PLLC</small></p>
      <p class="firm-tag">Attorneys At Law</p>
      <p class="firm-web">STANDWITHJUSTICE.COM</p>
      <p class="firm-phone">(555) 014-2290</p>
    </div>
    <div class="call-button">call now</div>
    <div class="portrait-ring"><div class="portrait" role="img" aria-label="Staff portrait photo"></div></div>
  </section>

</main>
</body>
</html>
```